Book Cover Design Project - Pickup and Seduction Book Cover Needed

We are a small pickup and dating company based in Sydney, Australia called Academy of Rapport.
We have almost finished our first book that will be complete and printed in the very near future.
The title of the book will be:
"Candid Courtship: Winning Hearts Through Plain Truth And Quiet Character"
With "Candid Courtship" being the book title
and
"Winning Hearts Through Plain Truth And Quiet Character" being the tagline.
The book is about being honest, sincere and authentic when meeting and dating women and we require a book cover that makes a great first impression and excites guys while still being very classy and stylish.
We look forward to any and all submissions and we also look forward to choosing the best one from the submissions.
The book cover size is standard 6x9
The cover needs to be for epub AND printed books.
When designing this, design random blurb words. We will add this in later
Bleed for the book is atleast .125
The book is around 250 pages in size
The author''s name is Lorcan Pettifer
Any other questions, please let me know
Reason: We want more submissions!
Dating

```html
<!DOCTYPE html>
<html lang="en">
<head>
<meta charset="utf-8">
<title>Candid Courtship — Lorcan Pettifer</title>
<link rel="stylesheet" href="https://fonts.googleapis.com/css2?family=Rubik:wght@800;900&family=Archivo+Black&display=swap">
<style>
  :root {
    --paper: #ffffff;
    --ink: #111111;
    --placeholder: #ececec;
  }
  html, body {
    margin: 0;
    padding: 0;
    overflow: hidden;
    background: var(--paper);
  }
  .cover {
    position: relative;
    width: 800px;
    height: 1200px;
    box-sizing: border-box;
    border: 1px solid var(--ink);
    background: var(--paper);
    overflow: hidden;
  }
  .title {
    position: absolute;
    left: 0;
    top: 112px;
    width: 100%;
    margin: 0;
    text-align: center;
    font-family: "Rubik", sans-serif;
    font-weight: 900;
    text-transform: uppercase;
    color: var(--paper);
    -webkit-text-stroke: 2px var(--ink);
    text-shadow: -6px -5px 0 var(--ink);
    line-height: 1;
  }
  .title-line {
    display: block;
  }
  .title-line--first {
    font-size: 150px;
    letter-spacing: 10px;
  }
  .title-line--second {
    font-size: 104px;
    letter-spacing: 4px;
    margin-top: 14px;
  }
  .author {
    position: absolute;
    left: 0;
    top: 424px;
    width: 100%;
    margin: 0;
    text-align: center;
    font-family: "Archivo Black", sans-serif;
    font-size: 22px;
    letter-spacing: 3px;
    text-transform: uppercase;
    color: var(--ink);
  }
  .door-art {
    position: absolute;
    left: 330px;
    top: 585px;
    width: 143px;
    height: 265px;
    background: var(--placeholder);
  }
  .tagline {
    position: absolute;
    left: 0;
    top: 1018px;
    width: 100%;
    margin: 0;
    text-align: center;
    font-family: "Archivo Black", sans-serif;
    font-size: 23px;
    line-height: 1.3;
    letter-spacing: 2px;
    text-transform: uppercase;
    color: var(--ink);
  }
</style>
</head>
<body>
  <main class="cover">
    <h1 class="title">
      <span class="title-line title-line--first">Candid</span>
      <span class="title-line title-line--second">Courtship</span>
    </h1>
    <p class="author">Lorcan Pettifer</p>
    <div class="door-art" role="img" aria-label="Line drawing of a door standing slightly ajar"></div>
    <p class="tagline">Winning Hearts Through Plain Truth<br>And Quiet Character</p>
  </main>
</body>
</html>
```